Information security software developer needs new product website

We are Quorvane - and we have created an anti-ransomware application that we think is pretty special.
Our product is now updating to version 2, bringing in a slew of new features that we want to showcase through this website.

The site itself should communicate trust and safety, be blue  (#22b8eb) and white and be themed around security, protection, shields and calmness. Due to the complex nature of the product, we will be creating a number of gifs to show usage of the features - the design needs to account for these gifs alongside feature headings.

Ideally, some graphics that communicate the themes of security and protection can be used throughout the design rather then technology photos - ultimately we don't want to scare people into using our product, we want it to feel like a trusted platform that makes sense to use.

you can read about us here - docs.quorvane-example.io to get an idea of what we do!

```html
<!DOCTYPE html>
<html lang="en">
<head>
<meta charset="utf-8">
<title>Quorvane — Anti-Ransomware</title>
<link rel="stylesheet" href="https://fonts.googleapis.com/css2?family=Poppins:wght@400;500&family=Fira+Sans:wght@400;500;600&family=Merriweather:wght@400&family=Oxygen:wght@400;700&display=swap">
<style>
:root{
  --ink:#05060f;
  --navy:#0a1230;
  --deep:#0a3d74;
  --glow:#0b6fc4;
  --brand:#1f8fd6;
  --sky:#22b8eb;
  --white:#ffffff;
  --muted:#c9d3e0;
  --card:#082a4f;
}
*{margin:0;padding:0;box-sizing:border-box}
html,body{width:1200px;height:2715px;overflow:hidden}
body{
  position:relative;
  font-family:"Poppins",sans-serif;
  color:var(--white);
  background:linear-gradient(180deg,#0a0f26 0%,#0a1a3c 9%,#0a3a70 20%,#0b64b4 28%,#0a5da8 38%,#062a55 44%,#040918 52%,var(--ink) 100%);
}
.abs{position:absolute}
a{color:inherit;text-decoration:none}

/* header */
.brand{display:flex;align-items:center;gap:14px;font-family:"Fira Sans",sans-serif;font-weight:500;color:var(--brand)}
.brand-mark{width:36px;height:36px;background:var(--brand);border-radius:4px}
.site-brand{left:60px;top:22px;font-size:50px;line-height:1}
.nav{right:62px;top:30px;display:flex;align-items:center;font-size:12px;letter-spacing:.2px}
.nav a{margin-left:22px;position:relative}
.nav a.active{color:var(--sky)}
.nav a.active::after{content:"";position:absolute;left:50%;top:22px;width:4px;height:4px;border-radius:50%;background:var(--sky);transform:translateX(-50%)}
.nav .sep{width:1px;height:22px;background:#3a4a6a;margin-left:22px}
.nav .login{color:var(--sky)}
.nav .start{background:var(--brand);border-radius:20px;padding:11px 18px;font-family:"Fira Sans",sans-serif;font-weight:500;font-size:14px;letter-spacing:.6px}

/* hero */
.hero-anti{left:0;width:1200px;top:132px;text-align:center;font-family:"Oxygen",sans-serif;font-weight:700;font-size:94px;letter-spacing:10px;color:rgba(60,120,190,.45)}
.hero-title{left:0;width:1200px;top:232px;text-align:center;font-family:"Fira Sans",sans-serif;font-weight:600;font-size:64px;color:var(--brand)}
.hero-sub{left:0;width:1200px;top:307px;text-align:center;font-family:"Merriweather",serif;font-size:18px;color:var(--muted)}
.hero-devices{left:337px;top:360px;width:522px;height:304px;border-radius:6px;background:linear-gradient(180deg,#eef1f5 0%,#dfe5ec 70%,#8c98a8 100%)}
.orbit{left:0;top:320px}

/* intro */
.intro-art{left:60px;top:730px;width:446px;height:436px;border-radius:8px;background:radial-gradient(ellipse at 60% 55%,#e9eef6 0%,#3aa6e6 35%,rgba(11,100,180,.2) 70%,transparent 75%)}
.intro-title{left:599px;top:804px;font-family:"Fira Sans",sans-serif;font-weight:500;font-size:46px}
.intro-copy{left:599px;top:870px;width:460px;font-size:11.6px;line-height:20px}
.intro-copy p{margin-bottom:14px}
.btn-outline{border:2px solid var(--white);border-radius:22px;text-align:center;font-family:"Fira Sans",sans-serif}
.learn{left:599px;top:1122px;width:143px;height:42px;line-height:38px;font-size:15px}

/* features */
.features-title{left:0;width:1200px;top:1264px;text-align:center;font-family:"Fira Sans",sans-serif;font-weight:500;font-size:44px;color:var(--brand)}
.feature-row{left:106px;top:1370px;width:988px;display:flex}
.feature{flex:1;display:flex;flex-direction:column;align-items:center;border-right:1px solid #1a2540;height:108px}
.feature:last-child{border-right:none}
.feature-icon{width:30px;height:30px;border:5px solid var(--brand);border-radius:4px;margin-bottom:14px}
.feature-name{font-family:"Fira Sans",sans-serif;font-size:12.5px;line-height:19.5px;text-align:center;width:130px}
.feature.active .feature-name{color:var(--brand)}

/* detail */
.detail-title{left:114px;top:1568px;width:420px;font-family:"Fira Sans",sans-serif;font-size:33px;line-height:43px;color:var(--brand)}
.detail-copy{left:114px;top:1664px;width:404px;font-size:11.6px;line-height:19.6px}
.detail-copy p{margin-bottom:14px}
.detail-copy .note{color:var(--brand);font-style:italic;font-size:14px;line-height:22px}
.detail-shot{left:574px;top:1658px;width:567px;height:323px;border-radius:14px;background:linear-gradient(180deg,#cfd4da 0%,#f4f6f8 15%,#ffffff 60%,#aab2bc 100%)}

/* download */
.download-card{left:132px;top:2168px;width:938px;height:282px;border-radius:22px;background:var(--card)}
.download-title{left:221px;top:2222px;font-family:"Fira Sans",sans-serif;font-size:35px;color:var(--brand)}
.download-copy{left:222px;top:2276px;width:340px;font-size:14px;line-height:21px}
.download-btn{left:217px;top:2342px;width:263px;height:42px;line-height:38px;font-size:15px;border-color:var(--brand);color:var(--brand)}
.download-art{left:616px;top:2145px;width:375px;height:305px;border-radius:50%;background:radial-gradient(ellipse at 50% 55%,#ffffff 0%,#2fb3ec 35%,#0d4f8e 65%,transparent 72%)}

/* footer */
.footer-brand{left:60px;top:2498px;font-size:46px}
.footer-about{left:62px;top:2554px;width:245px;font-size:11.6px;line-height:20px;color:var(--muted)}
.footer-col h4{font-family:"Fira Sans",sans-serif;font-weight:400;font-size:16px;color:var(--brand);margin-bottom:18px}
.footer-col li{list-style:none;font-size:11.6px;line-height:22.5px;color:var(--muted)}
.contact-line{display:flex;align-items:center;gap:12px;font-size:13.5px;margin-bottom:14px;color:var(--muted)}
.contacts{left:335px;top:2497px}
.links{left:612px;top:2497px}
.support{left:887px;top:2497px}
.copyright{left:0;width:1200px;top:2685px;text-align:center;font-size:11.6px;color:var(--muted)}
.copyright span{color:var(--brand)}
</style>
</head>
<body>

<header>
  <a class="abs brand site-brand" href="#"><span class="brand-mark"></span>Quorvane</a>
  <nav class="abs nav">
    <a class="active" href="#">HOME</a>
    <a href="#">FEATURES</a>
    <a href="#">PRODUCTS</a>
    <a href="#">CONTACT US</a>
    <span class="sep"></span>
    <a class="login" href="#">LOGIN</a>
    <a class="start" href="#">GET STARTED</a>
  </nav>
</header>

<section class="hero">
  <svg class="abs orbit" width="1200" height="340" viewBox="0 0 1200 340" aria-hidden="true">
    <path d="M0 30 C120 40 200 140 200 140 C260 240 340 280 420 300" fill="none" stroke="#1d4f86" stroke-width="1"/>
    <path d="M1200 20 C1080 40 1000 140 1000 140 C940 240 860 280 780 300" fill="none" stroke="#1d4f86" stroke-width="1"/>
    <circle cx="200" cy="142" r="6" fill="#2a7bc6"/>
    <circle cx="998" cy="136" r="6" fill="#2a7bc6"/>
  </svg>
  <div class="abs hero-anti">ANTI-</div>
  <h1 class="abs hero-title">RANSOMWARE</h1>
  <p class="abs hero-sub">Removes all Kind Threats and Protects PC</p>
  <div class="abs hero-devices" role="img" aria-label="Laptop and phone showing the Quorvane Access Manager password details screen"></div>
</section>

<section class="intro">
  <div class="abs intro-art" role="img" aria-label="Illustration of a hooded figure typing on a laptop atop a secure platform, surrounded by masked password bubbles"></div>
  <h2 class="abs intro-title">Quorvane</h2>
  <div class="abs intro-copy">
    <p>Quorvane Access Manager is a tool that allows you to safely delegate sensitive administrative access to computers in your Core Directory environment in a modern and user-friendly way.</p>
    <p>It provides a web-based interface that allows users to request local admin passwords, disk recovery keys, and grant just-in-time administrative access to their own accounts.</p>
    <p>It is fully compatible and works out-of-the-box with Helvane LAPW, or you can replace the Helvane LAPW agent with the Quorvane Access Manager Agent, which encrypts local admin passwords in the directory, and can optionally save a history of local admin passwords.</p>
  </div>
  <a class="abs btn-outline learn" href="#">LEARN MORE</a>
</section>

<section class="features">
  <h2 class="abs features-title">Features</h2>
  <div class="abs feature-row">
    <div class="feature active"><span class="feature-icon"></span><span class="feature-name">Web-based Access to Local Admin Passwords</span></div>
    <div class="feature"><span class="feature-icon"></span><span class="feature-name">Access Historical Local Admin Passwords</span></div>
    <div class="feature"><span class="feature-icon"></span><span class="feature-name">Just-in-time Administrative Access to Computers</span></div>
    <div class="feature"><span class="feature-icon"></span><span class="feature-name">Easy Access to DiskVault Recovery Passwords</span></div>
    <div class="feature"><span class="feature-icon"></span><span class="feature-name">Audit Success and Failure Event Logs</span></div>
    <div class="feature"><span class="feature-icon"></span><span class="feature-name">Modern Authentication Options</span></div>
  </div>
</section>

<section class="detail">
  <h3 class="abs detail-title">Web-based Access to Local Admin Passwords</h3>
  <div class="abs detail-copy">
    <p>Access Manager provides a simple web-based and mobile-friendly interface for accessing local admin passwords. There's no need for admins to install custom software, or have access to directory administrative tools to access LAPW passwords.</p>
    <p>Administrators also have the option of forcing an expiry time when a password is accessed. This ensures that the password is rotated after use.</p>
    <p>We use LAPW passwords ourselves, so we know they can be painful at times. We try to take away as much of that pain as possible. From using fonts where you can actually see the difference between an lower- case L and a capital I, to showing a breakdown of the password using the phonetic alphabet to make it easy to read it out to someone. Ever find yourself needing to type a LAPW password into a Panes logon screen? Have access manager read the password to you while you type!</p>
    <p class="note">Whether you use Helvane LAPW, or the Quorvane Access Manager agent, the user experience is the same.</p>
  </div>
  <div class="abs detail-shot" role="img" aria-label="Laptop showing the Access Manager request access form"></div>
</section>

<section class="download">
  <div class="abs download-card"></div>
  <h3 class="abs download-title">Download The App</h3>
  <p class="abs download-copy">Defend Against Ransomware and Other Lateral Movement-Based Attacks</p>
  <a class="abs btn-outline download-btn" href="#">Download The Current Release</a>
  <div class="abs download-art" role="img" aria-label="Illustration of a figure at a laptop on a platform encircled by protective security panels"></div>
</section>

<footer>
  <div class="abs brand footer-brand"><span class="brand-mark"></span>Quorvane</div>
  <p class="abs footer-about">To reduce the likelihood and impact of a wide-spread compromise in your environ-ment by removing permanent...</p>
  <div class="abs footer-col contacts">
    <h4>Contact Us</h4>
    <div class="contact-line">
      <svg width="18" height="18" viewBox="0 0 24 24" aria-hidden="true"><path d="M6.6 10.8a15.1 15.1 0 0 0 6.6 6.6l2.2-2.2a1 1 0 0 1 1-.25 11.4 11.4 0 0 0 3.6.57 1 1 0 0 1 1 1V20a1 1 0 0 1-1 1A17 17 0 0 1 3 4a1 1 0 0 1 1-1h3.5a1 1 0 0 1 1 1c0 1.25.2 2.45.57 3.57a1 1 0 0 1-.25 1z" fill="#1f8fd6"/></svg>
      123 456 7890
    </div>
    <div class="contact-line">
      <svg width="18" height="18" viewBox="0 0 24 24" aria-hidden="true"><rect x="2" y="5" width="20" height="14" rx="2" fill="#1f8fd6"/><path d="M3 6l9 7 9-7" fill="none" stroke="#05060f" stroke-width="1.6"/></svg>
      info@quorvane-example.com
    </div>
  </div>
  <div class="abs footer-col links">
    <h4>Quick Links</h4>
    <ul><li>Home</li><li>Feature</li><li>Contact</li><li>Newsletter</li></ul>
  </div>
  <div class="abs footer-col support">
    <h4>Support</h4>
    <ul><li>Contact Support</li><li>Technical Documentation</li><li>FAQ</li><li>Trust Security</li></ul>
  </div>
  <p class="abs copyright">©<span>Quorvane</span> - 2021 All rights reserved.</p>
</footer>

</body>
</html>
```